Eye Doctor Website

We are looking for a new logo and update to our website.

The Practice Name is Dr. Helen Tarbeck and Associates

This is a simple straight forward project that requires some aspect of Optometry or eye care in the logo. Also we are located in Colorado so if we are open to the idea of adding some element of the Colorado state flag or image of the mountains

For the web all the text is already complete visit www.drhelentarbeck-example.com to see what we currently have we will be taking what you created and updating this site.

We would like the new logo to be used on the web and on business cards.

Please only submit the first page of the web site. Then we can get the rest from there.

Text does not need to be included for the design but would help.

Good luck and let us know if you have any questions

Target Market(s)

30-50 year olds looking for an eye exam.

Site must be fun but also serious and professional to catch the patients attention. Trying to play on outdoor theme

Industry/Entity Type

Flag

Font styles to use
Serif

Colors

Designer to choose colors to be used in the design.

Requirements
Must have
• Need a theme to play off of... Either use the state flag of Colorado or something with mountains. We are very close to the Rocky Mountains so this would work.

Want this them to play throughout the whole site and on Business cards
Nice to have
• Simple navigation. Don't need a lot of text
Should not have
• Clutter.... Simple to the point.

```html
<!DOCTYPE html>
<html lang="en">
<head>
<meta charset="utf-8">
<title>Dr. Helen Tarbeck and Associates</title>
<link href="https://fonts.googleapis.com/css2?family=Arvo&family=Open+Sans:wght@400;600&display=swap" rel="stylesheet">
<style>
:root{
  --blue:#1a6fb0;
  --blue-bright:#0d8fd6;
  --nav:#1c6ea9;
  --nav-active:#145a8c;
  --text:#6b6b6b;
  --grey-light:#ececec;
  --footer:#3f3e3e;
  --white:#ffffff;
}
*{box-sizing:border-box;margin:0;padding:0}
html,body{width:680px;height:1200px;overflow:hidden;background:var(--white)}
body{position:relative;font-family:"Open Sans",Arial,sans-serif;color:var(--text)}
.abs{position:absolute}

/* header */
.brand{left:50px;top:50px;display:flex;align-items:center;gap:14px}
.brand-mark{width:34px;height:34px;border-radius:50%;background:var(--blue)}
.brand-name{font-family:"Arvo",Georgia,serif;font-size:16px;line-height:25px;color:var(--blue);text-transform:uppercase;white-space:nowrap}
.call{right:50px;top:36px;text-align:right;padding-right:22px}
.call-label{font-size:11px;color:#666}
.call-number{font-size:14px;color:var(--blue)}
.call svg{position:absolute;right:0;top:6px}
.search{left:483px;top:84px;width:147px;height:20px;border:1px solid #ccc;font-size:8px;color:#888;padding:4px 7px}
.search svg{position:absolute;right:5px;top:5px}

/* nav */
.nav{left:50px;top:120px;width:581px;height:34px;background:var(--nav);display:flex}
.nav a{color:var(--white);text-decoration:none;font-size:10px;text-transform:uppercase;line-height:34px;text-align:center;white-space:nowrap;border-right:1px solid rgba(255,255,255,.18);flex:none}
.nav a.active{background:var(--nav-active)}
.nav a:last-child{border-right:0}

/* hero */
.hero{left:50px;top:154px;width:581px;height:217px;background:linear-gradient(180deg,#1f5ea4 0%,#4b8ccf 45%,#c9dbea 75%,#6b7f96 100%)}
.hero-portrait{position:absolute;right:0;top:0;width:200px;height:217px;background:linear-gradient(90deg,rgba(210,170,150,0) 0%,#d8aa92 40%,#7a4330 100%)}
.hero-text{position:absolute;left:17px;top:64px;font-size:16.5px;line-height:27px;color:var(--white)}
.hero-dots{position:absolute;left:18px;bottom:11px;display:flex;gap:5px}
.hero-dots span{width:8px;height:8px;border-radius:50%;background:rgba(255,255,255,.55)}
.hero-dots span:first-child{background:var(--white)}

/* feature thumbnails */
.feature{top:401px;width:180px;height:107px;border:1px solid #ddd;padding:4px;background:var(--white);box-shadow:0 0 3px rgba(0,0,0,.08)}
.feature-img{position:relative;width:100%;height:100%}
.feature-caption{position:absolute;left:0;right:0;bottom:0;height:20px;background:rgba(120,120,120,.55);color:var(--white);font-size:9px;font-weight:600;line-height:20px;padding-left:7px;text-transform:uppercase}

/* welcome */
.section-title{font-size:15px;font-weight:400;color:var(--blue);white-space:nowrap}
.welcome-photo{left:50px;top:579px;width:112px;height:92px;background:linear-gradient(180deg,#a9d3dd,#e2c59b)}
.welcome-text{left:183px;top:575px;width:200px;font-size:7.8px;line-height:14px;color:var(--text)}

/* services */
.service{left:50px;width:327px;height:27px;background:var(--grey-light);border:1px solid #ddd;border-radius:2px;font-size:8.5px;line-height:25px;padding-left:34px;color:#555;white-space:nowrap}
.service.active{background:var(--blue-bright);border-color:var(--blue-bright);color:var(--white)}
.service i{position:absolute;left:9px;top:6px;width:14px;height:14px;border-radius:50%;background:var(--white);font-style:normal;color:#888;font-size:11px;line-height:14px;text-align:center}
.service.active i{color:var(--blue-bright)}

/* appointment */
.appt{left:441px;top:545px;width:189px;height:311px;background:#f0f0f0;border:1px solid #e2e2e2}
.appt-head{height:63px;background:linear-gradient(180deg,#16aef0,#0a7fcf);color:var(--white);text-align:center;padding-top:11px}
.appt-title{font-size:14px}
.appt-phone{font-size:12.5px;margin-top:6px;display:flex;justify-content:center;align-items:center;gap:6px}
.field{position:absolute;left:10px;width:170px;height:24px;background:var(--white);border:1px solid #ccc;font-size:8px;color:#777;padding:6px 8px}
.submit{position:absolute;left:30px;top:266px;width:134px;height:27px;background:#9a9ea2;border-bottom:3px solid #7d8185;color:var(--white);font-size:11.5px;text-align:center;line-height:25px}

/* map + footer */
.map{left:0;top:893px;width:680px;height:168px;background:linear-gradient(160deg,#ece6da 0%,#e4ddd0 40%,#d9e3ea 55%,#ece6da 70%)}
.torn{left:0;top:1035px}
.footer{left:0;top:1055px;width:680px;height:145px;background:var(--footer);color:var(--white);font-family:Arial,sans-serif}
.footer h4{position:absolute;font-size:10px;font-weight:normal;top:27px}
.hours{position:absolute;left:76px;top:50px;font-size:8px;line-height:15px;white-space:nowrap}
.contact-list{position:absolute;left:282px;top:48px;font-size:8px;line-height:15px}
.contact-list li{list-style:none;position:absolute;left:19px;white-space:nowrap}
.contact-list svg{position:absolute;left:-19px;top:2px}
.social{position:absolute;left:442px;top:47px;display:flex;gap:7px}
.social span{width:21px;height:21px}
.footer-links{position:absolute;left:400px;top:80px;width:186px;text-align:center;font-size:7.8px;line-height:19px;white-space:nowrap}
</style>
</head>
<body>

<header>
  <div class="abs brand">
    <span class="brand-mark"></span>
    <div class="brand-name">Dr. Helen Tarbeck<br>and Associates</div>
  </div>
  <div class="abs call">
    <div class="call-label">Call today</div>
    <div class="call-number">+61 02 5550 1942</div>
    <svg width="16" height="22" viewBox="0 0 16 22"><path d="M3 1c2-1 3 0 4 3s0 4-1 5c1 3 3 6 5 7 1-1 2-2 4 0s1 4-1 5C8 23 0 11 3 1z" fill="#1a6fb0"/></svg>
  </div>
  <div class="abs search">Search..
    <svg width="9" height="9" viewBox="0 0 9 9"><circle cx="3.6" cy="3.6" r="2.8" fill="none" stroke="#999" stroke-width="1.2"/><line x1="5.6" y1="5.6" x2="8.5" y2="8.5" stroke="#999" stroke-width="1.3"/></svg>
  </div>
</header>

<nav class="abs nav">
  <a class="active" href="#" style="width:65px">Home</a>
  <a href="#" style="width:135px">About Dr. Tarbeck</a>
  <a href="#" style="width:163px">Schedule an Appointment</a>
  <a href="#" style="width:134px">Office Info/Specials</a>
  <a href="#" style="width:84px">Contact</a>
</nav>

<section class="abs hero" role="img" aria-label="Snowy mountain range under a blue sky beside a woman pointing at her eye">
  <div class="hero-portrait"></div>
  <p class="hero-text">Lorem ipsum dolor<br>sit amet consectetur<br>adipiscing elit.</p>
  <div class="hero-dots"><span></span><span></span><span></span><span></span></div>
</section>

<div class="abs feature" style="left:50px"><div class="feature-img" role="img" aria-label="Patient at an eye examination instrument" style="background:linear-gradient(90deg,#3a3a3a,#e9e9e9 55%,#c8a58e)"><span class="feature-caption">Lorem ipsum dolor</span></div></div>
<div class="abs feature" style="left:250px"><div class="feature-img" role="img" aria-label="Woman in glasses in front of an eye chart" style="background:linear-gradient(90deg,#c9ced2,#e3e5e6 45%,#7a4a34)"><span class="feature-caption">Lorem ipsum dolor</span></div></div>
<div class="abs feature" style="left:451px"><div class="feature-img" role="img" aria-label="Woman holding a pair of eyeglasses" style="background:linear-gradient(90deg,#c98d5e,#dcb69a 50%,#8a5a3f)"><span class="feature-caption">Lorem ipsum dolor</span></div></div>

<h2 class="abs section-title" style="left:50px;top:543px">Welcome to Our Website</h2>
<div class="abs welcome-photo" role="img" aria-label="Portrait of Dr. Helen Tarbeck"></div>
<p class="abs welcome-text">Welcome to Dr. Helen Tarbeck's optometry office. We are conveniently located in Pinecrest Plaza in Alder Springs, CO. We are here to provide you and your family with affordable, thorough eye care. Our office employs the latest in eye care technology in order to provide a superior quality of care.</p>

<h2 class="abs section-title" style="left:50px;top:693px">Services</h2>
<div class="abs service active" style="top:725px"><i>+</i>Comprehensive eye exams with testing for glaucoma, cataracts.</div>
<div class="abs service" style="top:759px"><i>+</i>Contact lens exams, including astigmatism (toric), bifocal and gas lenses.</div>
<div class="abs service" style="top:793px"><i>+</i>Treatment of eye infections, dry eyes, and other eye problems</div>
<div class="abs service" style="top:827px"><i>+</i>Diabetic eye exams</div>

<aside class="abs appt">
  <div class="appt-head">
    <div class="appt-title">Make an Appointment</div>
    <div class="appt-phone">
      <svg width="14" height="12" viewBox="0 0 14 12"><path d="M1 4c0-3 12-3 12 0v1h-3V3.5H4V5H1z" fill="#fff"/><rect x="2.5" y="5.5" width="9" height="6" rx="1" fill="#fff"/><circle cx="7" cy="8.5" r="1.6" fill="#0a7fcf"/></svg>
      1-800-555-0199
    </div>
  </div>
  <div class="field" style="top:78px">Name</div>
  <div class="field" style="top:116px">Phone</div>
  <div class="field" style="top:152px">E-mail</div>
  <div class="field" style="top:188px;height:67px">Message</div>
  <div class="submit">Submit Request</div>
</aside>

<div class="abs map" role="img" aria-label="Street map showing the office location"></div>
<svg class="abs torn" width="680" height="22" viewBox="0 0 680 22" aria-hidden="true">
  <path d="M0 14 L12 10 L20 13 L30 8 L42 12 L55 9 L66 13 L80 7 L92 11 L104 9 L118 13 L130 8 L145 12 L158 10 L170 13 L184 8 L198 12 L210 9 L224 13 L238 8 L250 11 L264 9 L278 13 L290 7 L304 12 L318 9 L330 13 L344 8 L358 11 L372 9 L386 13 L398 8 L412 12 L426 9 L440 13 L452 7 L466 11 L480 9 L494 13 L506 8 L520 12 L534 10 L548 13 L560 8 L574 12 L588 9 L600 13 L614 8 L628 11 L642 9 L656 13 L668 9 L680 12 L680 22 L0 22 Z" fill="#3f3e3e"/>
</svg>

<footer class="abs footer">
  <h4 style="left:76px">Working Hours</h4>
  <div class="hours">
    Monday - 10:00am - 6:00pm<br>
    Wednesday - 10:00am - 7:00pm<br>
    Friday - 10:00am - 6:00pm<br>
    Saturday - 9:00am - 5:00pm<br>
    Sunday - 1:00pm - 4:00pm (every other week)
  </div>

  <h4 style="left:282px">Contact</h4>
  <ul class="contact-list">
    <li style="top:0">
      <svg width="8" height="11" viewBox="0 0 8 11"><path d="M4 0a4 4 0 0 1 4 4c0 3-4 7-4 7S0 7 0 4a4 4 0 0 1 4-4z" fill="#bbb"/><circle cx="4" cy="4" r="1.4" fill="#3f3e3e"/></svg>
      1420 Ridgeway Ave.<br>Alder Springs CO 80299
    </li>
    <li style="top:32px">
      <svg width="11" height="8" viewBox="0 0 11 8"><rect width="11" height="8" fill="#bbb"/><path d="M0 0l5.5 4.5L11 0" fill="none" stroke="#3f3e3e" stroke-width="1"/></svg>
      info@tarbeck-example.com
    </li>
    <li style="top:56px">
      <svg width="9" height="10" viewBox="0 0 9 10"><path d="M1.5 0.5c1-.5 1.5 0 2 1.5s0 2-.5 2.5c.5 1.5 1.5 2.5 2.5 3 .5-.5 1-1 2-.2s.5 2-.5 2.4C3.5 10.5 0 5 1.5.5z" fill="#bbb"/></svg>
      55 501 2684
    </li>
  </ul>

  <div class="social" aria-label="Social links">
    <span style="background:#3b5998"></span>
    <span style="background:#2a9fd8"></span>
    <span style="background:#f26b22"></span>
    <span style="background:#d4302b"></span>
    <span style="background:#6fb9e6"></span>
  </div>
  <div class="footer-links">
    Terms and Conditions | Privacy Policy | Site Map<br>
    © 2013 Copyrights. All Rights Reserved.
  </div>
</footer>

</body>
</html>
```